Corvane Summit 2018 Conference flyer

We require a professionally designed flyer for printing and soft copy distributing. The current flyer attached with the information that is required. We need a modern, eye catching flyer to accompany the banner. The banner should represent what the conference is all about. We require the Corvane Lab colours as featured in the current banner. The information needs to be legible and well spaced out so people can find the information quickly.

Target Market(s)

Relating to healthcare professionals, scientists, engineers

Font styles to use
Sans Serif

```html
<!DOCTYPE html>
<html lang="en">
<head>
<meta charset="utf-8">
<title>Corvane Summit 2018 Conference</title>
<link href="https://fonts.googleapis.com/css2?family=Roboto:wght@400;500;700&family=Oswald:wght@600;700&display=swap" rel="stylesheet">
<style>
:root{
  --pink:#e5137a;
  --pink-dark:#d20f6e;
  --navy:#2b3990;
  --navy-deep:#1c2456;
  --ink:#222;
  --sand:#ded8cf;
  --yellow:#ffe600;
  --bg:#e4e4e4;
}
*{margin:0;padding:0;box-sizing:border-box}
html,body{width:1200px;height:1200px;overflow:hidden;background:var(--bg);font-family:"Roboto",sans-serif}
.flyer{position:absolute;left:156px;top:30px;width:888px;height:1141px;background:#fff;overflow:hidden}
.abs{position:absolute}
.top-band{left:0;top:0;width:888px;height:59px;background:var(--pink)}
.top-rule{left:0;top:63px;width:888px;height:4px;background:#c9c9c9}
.tab-left{left:0;top:118px;width:49px;height:64px;background:var(--pink)}
.tab-right{right:0;top:118px;width:33px;height:64px;background:var(--pink)}
.annual{left:83px;top:108px;color:var(--navy);font-weight:500;font-size:62px;line-height:1}
.annual sup{font-size:34px;vertical-align:top;position:relative;top:-2px}
.topics{left:83px;top:200px;color:var(--navy);font-weight:500;font-size:24px;line-height:33px}
.event-name{left:480px;top:118px;width:230px;text-align:left}
.event-name .brand{display:inline-block;color:var(--pink);font-weight:700;font-size:52px;line-height:62px;letter-spacing:-1px}
.event-name .country{color:var(--navy);font-weight:700;font-size:29px;letter-spacing:2px;line-height:30px}
.event-name .kind{color:var(--navy);font-weight:700;font-size:19px;letter-spacing:6px;line-height:22px}
.event-name .year{color:var(--navy);font-weight:700;font-size:78px;line-height:76px}
.hero-hand{left:700px;top:62px;width:155px;height:254px;background:linear-gradient(160deg,#3a4fb8,#1e2a88);border-radius:40px 40px 20px 60px}
.header-rule{left:0;top:318px;width:888px;height:7px;background:var(--pink)}
.photo-models{left:0;top:329px;width:520px;height:344px;background:linear-gradient(135deg,#efecea 0%,#d9d2cf 45%,#b8b6c6 100%)}
.photo-scan{left:529px;top:329px;width:359px;height:344px;background:radial-gradient(circle at 50% 45%,#3d2a6a 0%,#12121a 60%,#000 100%)}
.invite{left:50px;top:673px;width:792px;height:101px;background:linear-gradient(#3c4f9a,#1c2456 70%,#10163a);color:#fff;text-align:center;font-size:26px;line-height:33px;padding-top:16px;border:2px solid #c9cbe0;border-top:0}
.lead{left:0;top:782px;width:888px;text-align:center;color:var(--navy);font-weight:500;font-size:28px}
.aims{left:74px;top:822px;list-style:none;color:var(--ink);font-size:19px;line-height:25.5px}
.aims li{display:flex;align-items:center;gap:11px}
.aims svg{width:20px;height:20px;flex:none}
.info-band{left:0;top:938px;width:888px;height:120px;background:var(--pink);color:#fff}
.col{position:absolute;top:0;height:120px;padding-top:8px}
.col.when{left:0;width:198px;padding-left:68px}
.col.where{left:198px;width:179px;padding-left:18px;background:var(--pink-dark)}
.col.time{left:377px;width:128px;padding-left:15px}
.col.links{left:505px;width:383px;padding-left:30px;background:var(--pink-dark);padding-top:16px}
.col h3{font-weight:500;font-size:34px;line-height:36px}
.col p{font-size:18px;line-height:22px;font-weight:500}
.col.where p{font-size:13.5px;line-height:17px;font-weight:500}
.col.time p{font-size:20px;line-height:24px}
.col.links p{font-size:13.5px;line-height:22px}
.code-label{left:505px;top:1020px;width:383px;text-align:center;font-family:"Oswald",sans-serif;font-weight:700;font-size:21px;color:var(--yellow);letter-spacing:.5px}
.foot{left:0;top:1058px;width:888px;height:83px;background:var(--sand)}
.partner{position:absolute;display:flex;align-items:center;gap:7px;color:#1f2a2a;font-family:"Roboto",sans-serif;white-space:nowrap}
.partner.fabricore{left:70px;top:30px;font-size:17px;font-weight:500}
.partner.fabricore .mark{width:10px;height:10px;background:#1e8ccf}
.partner.harrowgate{left:180px;top:28px;font-size:19px;font-weight:400;color:#16605a}
.partner.harrowgate .mark{width:14px;height:14px;border-radius:50%;background:#16605a}
.badge{position:absolute;left:400px;top:12px;width:40px;height:46px;background:#2c3a6e;border-radius:3px}
.offer{left:505px;top:1066px;width:383px;text-align:center;font-family:"Oswald",sans-serif;font-weight:600;font-size:19px;line-height:24px;color:#1b1b1b;letter-spacing:.4px}
</style>
</head>
<body>
<main class="flyer">
  <div class="abs top-band"></div>
  <div class="abs top-rule"></div>
  <div class="abs tab-left"></div>
  <div class="abs tab-right"></div>

  <h1 class="abs annual">4<sup>TH</sup> ANNUAL</h1>
  <div class="abs topics">3D PRINTING<br>3D MODELLING<br>VIRTUAL REALITY</div>

  <div class="abs event-name">
    <div class="brand">Corvane</div>
    <div class="country">SUMMIT</div>
    <div class="kind">CONFERENCE</div>
    <div class="year">2018</div>
  </div>
  <div class="abs hero-hand" role="img" aria-label="Blue 3D-printed prosthetic hand reaching down"></div>

  <div class="abs header-rule"></div>
  <div class="abs photo-models" role="img" aria-label="Collection of colourful 3D-printed anatomical models: arteries, brain, heart and prosthetic hand"></div>
  <div class="abs photo-scan" role="img" aria-label="Virtual reality render of coloured blood vessels and organs on black"></div>

  <div class="abs invite">The @CorvaneLab at Harrowgate Health warmly invites you<br>to attend the 2018 Corvane Summit Symposium.</div>

  <h2 class="abs lead">THIS CROSS-DISCIPLINARY EVENT WILL :</h2>
  <ul class="abs aims">
    <li><svg viewBox="0 0 20 20"><path d="M2 11 L7 17 L18 2" fill="none" stroke="#2b3990" stroke-width="3.4" stroke-linecap="round" stroke-linejoin="round"/></svg>Showcase clinical applications of 3d modelling and printing</li>
    <li><svg viewBox="0 0 20 20"><path d="M2 11 L7 17 L18 2" fill="none" stroke="#2b3990" stroke-width="3.4" stroke-linecap="round" stroke-linejoin="round"/></svg>Explore the use of Virtual Reality in Medicine</li>
    <li><svg viewBox="0 0 20 20"><path d="M2 11 L7 17 L18 2" fill="none" stroke="#2b3990" stroke-width="3.4" stroke-linecap="round" stroke-linejoin="round"/></svg>Bring together clinicians, engineers and thought leaders in medical 3D printing</li>
    <li><svg viewBox="0 0 20 20"><path d="M2 11 L7 17 L18 2" fill="none" stroke="#2b3990" stroke-width="3.4" stroke-linecap="round" stroke-linejoin="round"/></svg>Discuss social and legal issues in medical 3d printing</li>
  </ul>

  <section class="abs info-band">
    <div class="col when"><h3>When:</h3><p>Saturday 13<br>&amp; Sunday 14<br>October 2018</p></div>
    <div class="col where"><h3>Where:</h3><p>Northbank Neuro Centre<br>Halden Wing Building<br>88/12 Cressway Parade<br>LINFORD VIC 3999</p></div>
    <div class="col time"><h3>Time:</h3><p>Starting<br>at 0900hrs</p></div>
    <div class="col links"><p>More info: https://corvanelab.org.au/summit18/<br>Registration: https://corvanelab.org.au/registration/<br>Enquiries: printlab@harrowgate.org.au</p></div>
  </section>
  <div class="abs code-label">DISCOUNT CODE:</div>

  <footer class="abs foot">
    <div class="partner fabricore"><span class="mark"></span>fabricore</div>
    <div class="partner harrowgate"><span class="mark"></span>Harrowgate Health</div>
    <div class="badge"></div>
  </footer>
  <div class="abs offer">Get 50% off your ticket if you enter<br>3DPROMO</div>
</main>
</body>
</html>
```